HiItsJonBrell.com needs a modern, eye-catching business card design

My name is Jon Brell and I own a video training (software development industry) website. I need a business card design that is eye catching for when I travel to conferences or do seminars. I would prefer something simple but bold. Something along the lines of this: https://pixvaultstatic.example/gallery_img/530172/44018/44018_9917302_530172_image.jpg

Note that I do not have a specific logo, but I do have an caricature I use on my site of myself. I've not attached it because I'm not really a fan of having it on my business cards. I would prefer lettering instead of an image. You can go to my website (https://hiitsjonbrell.com) for inspiration.

I want to add the following information on my card (the order of these, their size, and their casing is up to you):

Jon Brell
jon@HiItsJonBrell.com
@HiItsJonBrell
HiItsJonBrell.com
vidsharehub.example/HiItsJonBrell

I would also like to have somewhere on the card a small ad that says "Get a free course at https://HiItsJonBrell.com/FreeCourse". Feel free to play with that wording or layout if you need. I would prefer this text to be at the bottom of the card and subtle. Some small eye-catching thing might be ok but nothing huge or garish.

I plan on printing this card at pressquill.example (https://www.pressquill.example/us/design-guidelines/business-cards.html). I would like it to be the standard size (3.66" x 2.16"). I would prefer rounded corners and horizontal orientation. This is a two-side design. I would prefer the side with all of the information be primarily white but I like color text (again, flexible on that). On the front side, I like simple. Maybe just HiItsJonBrell.com (casing on that is up to you - whatever looks and reads the best - that goes for all of the casing). As for font choices, I prefer a modern, clean font. For example, Open Sans Light can be a nice option.

Website Info (might be helpful for the card):
Color Palette

Darkest blue - #263246
Alternate blue - #2F4E6A
Light blue - #2A98C3
Orange - #FF6201
White - #FFFFFF

Font for Jon Brell Logo

Jellyka Estryas Handwriting
http://www.typecrate.example/jellyka_estryas_handwriting.font

Fonts for Site Content and VidShare Thumbnails

Lovelo (bold title font)
http://www.glyphmill.example/lovelo-font/

Open Sans (body font)
http://www.letterbarn.example/fonts/open-sans

Industry/Entity Type

Software Development

Contact Information for Business Card

Jon Brell
jon@HiItsJonBrell.com
@HiItsJonBrell
HiItsJonBrell.com
vidsharehub.example/HiItsJonBrell

Get a free course at https://HiItsJonBrell.com/FreeCourse

Colors

Designer to choose colors to be used in the design.

Requirements
Nice to have
• Modern color - maybe primarily a color on the front and then that color as an accent on the back.
Should not have
• Lots of colors - I LOVE color but do not want a rainbow of colors on the card.

```html
<!DOCTYPE html>
<html lang="en">
<head>
<meta charset="utf-8">
<title>HiItsJonBrell.com Business Card</title>
<link href="https://fonts.googleapis.com/css2?family=Open+Sans:wght@400;600;700&family=Oswald:wght@500&display=swap" rel="stylesheet">
<style>
  :root {
    --stage-bg: #e8e5e1;
    --brand-blue: #2A98C3;
    --brand-blue-light: #5cb6d8;
    --card-white: #ffffff;
    --ink-dark: #2b2b2b;
    --ink-mid: #444444;
  }
  * { margin: 0; padding: 0; box-sizing: border-box; }
  html, body {
    width: 1200px; height: 1000px; overflow: hidden;
    background: var(--stage-bg);
    font-family: "Open Sans", Arial, sans-serif;
  }
  .stage { position: relative; width: 1200px; height: 1000px; }

  .card {
    position: absolute; left: 266px; width: 666px; height: 397px;
    border-radius: 28px;
    box-shadow: 0 4px 14px rgba(0,0,0,0.18);
    overflow: hidden;
  }
  .card-front { top: 74px; background: var(--brand-blue); }
  .card-back { top: 533px; background: var(--card-white); }

  .caricature-area {
    position: absolute; left: 170px; top: 60px; width: 330px; height: 300px;
    border-radius: 50%;
    background: radial-gradient(circle, rgba(255,255,255,0.35) 0%, rgba(255,255,255,0.12) 45%, rgba(255,255,255,0) 70%);
  }
  .brand-name {
    position: absolute; left: 0; right: 0; top: 176px;
    text-align: center;
    color: var(--card-white);
    font-weight: 600; font-size: 50px; letter-spacing: 0.5px;
  }
  .free-course {
    position: absolute; left: 0; right: 0; top: 349px;
    text-align: center; color: var(--card-white);
    font-size: 16px; font-weight: 400;
  }
  .free-course strong { font-weight: 700; }

  .identity {
    position: absolute; right: 392px; top: 163px; text-align: right;
  }
  .identity-name {
    font-family: "Oswald", "Arial Narrow", sans-serif;
    font-weight: 500; font-size: 40px; line-height: 44px;
    color: var(--brand-blue); letter-spacing: 0.5px;
  }
  .identity-role { font-size: 15px; color: var(--ink-mid); margin-top: 2px; }
  .divider {
    position: absolute; left: 290px; top: 167px; width: 2px; height: 66px;
    background: var(--brand-blue);
  }
  .contact-list {
    position: absolute; left: 308px; top: 161px; list-style: none;
  }
  .contact-list li {
    display: flex; align-items: center; gap: 7px;
    font-size: 16px; line-height: 25px; color: var(--ink-dark);
  }
  .contact-list svg { width: 14px; height: 14px; flex: none; }
  .plain-square { width: 12px; height: 12px; background: var(--brand-blue); border-radius: 2px; margin: 0 1px; flex: none; }
  .social {
    position: absolute; left: 0; right: 0; top: 344px;
    display: flex; justify-content: center; align-items: center; gap: 8px;
    font-size: 16px; font-weight: 700; color: var(--ink-dark);
  }
  .social-dot { width: 18px; height: 18px; border-radius: 50%; background: var(--brand-blue); }
</style>
</head>
<body>
<main class="stage">
  <section class="card card-front">
    <div class="caricature-area" role="img" aria-label="Caricature illustration of Jon Brell on a halftone dot burst"></div>
    <div class="brand-name">HiItsJonBrell.com</div>
    <p class="free-course"><strong>Get a free course at</strong> https://HiItsJonBrell.com/FreeCourse</p>
  </section>

  <section class="card card-back">
    <div class="identity">
      <div class="identity-name">JON BRELL</div>
      <div class="identity-role">Owner / CEO</div>
    </div>
    <div class="divider"></div>
    <ul class="contact-list">
      <li>
        <svg viewBox="0 0 14 14" aria-hidden="true"><rect x="1" y="3" width="12" height="8" fill="var(--brand-blue)"/><path d="M1 3 L7 8 L13 3" fill="none" stroke="#fff" stroke-width="1.2"/></svg>
        jon@HiItsJonBrell.com
      </li>
      <li>
        <svg viewBox="0 0 14 14" aria-hidden="true"><circle cx="7" cy="7" r="6" fill="none" stroke="var(--brand-blue)" stroke-width="1.4"/><ellipse cx="7" cy="7" rx="2.6" ry="6" fill="none" stroke="var(--brand-blue)" stroke-width="1.1"/><line x1="1" y1="7" x2="13" y2="7" stroke="var(--brand-blue)" stroke-width="1.1"/></svg>
        HiItsJonBrell.com
      </li>
      <li>
        <span class="plain-square" aria-hidden="true"></span>
        vidsharehub.example/HiItsJonBrell
      </li>
    </ul>
    <div class="social">
      <span class="social-dot" aria-hidden="true"></span>
      <span>@HiItsJonBrell</span>
    </div>
  </section>
</main>
</body>
</html>
```